Chiropractor needs a snazzy business card

Business card for a chiropractic office.
Office treats patients of all ages.
Focus is on a natural lifestyle.
Colors can include the logo colors as well as white and a little orange.
Ideally the card would have something chiropractic related such as a spine.

The back of the card should have a items for making appointments (date, times....)

```html
<!DOCTYPE html>
<html lang="en">
<head>
<meta charset="UTF-8">
<title>Meridian Chiropractic – Business Card</title>
<link href="https://fonts.googleapis.com/css2?family=Open+Sans:wght@400;600&display=swap" rel="stylesheet">
<style>
  :root {
    --navy: #0d4a80;
    --navy-deep: #0a3d6b;
    --green: #4cb848;
    --green-soft: #a9d9a2;
    --orange: #f28c1e;
    --paper: #ffffff;
    --paper-grey: #e4e6e8;
    --ink: #1f3f6a;
    --stage: #eceae6;
    --bone: #e9e0c8;
  }
  * { box-sizing: border-box; margin: 0; padding: 0; }
  html, body { width: 1200px; height: 1023px; overflow: hidden; }
  body {
    background: var(--stage);
    font-family: "Open Sans", Arial, sans-serif;
    position: relative;
  }
  .card {
    position: absolute;
    width: 560px;
    height: 320px;
    overflow: hidden;
    box-shadow: 0 10px 28px rgba(0,0,0,0.22);
  }

  /* Front */
  .card-front { left: 70px; top: 110px; background: var(--paper); }
  .front-spine {
    position: absolute; right: 0; top: 0;
    width: 300px; height: 118px;
    background: radial-gradient(ellipse at 60% 30%, var(--bone) 0%, #f3eee2 45%, rgba(255,255,255,0) 75%);
  }
  .front-brand {
    position: absolute; left: 40px; top: 112px;
    color: var(--navy);
    font-weight: 600;
    font-size: 27px;
    line-height: 1.1;
    letter-spacing: 1px;
    text-transform: uppercase;
  }
  .front-brand span { display: block; font-size: 19px; letter-spacing: 3px; }
  .person { position: absolute; left: 40px; top: 200px; }
  .person-name { color: var(--navy); font-size: 21px; letter-spacing: 1.5px; }
  .person-role { color: var(--orange); font-size: 14px; margin-left: 90px; }
  .accent-tab {
    position: absolute; left: 40px; top: 254px;
    width: 44px; height: 14px; border-radius: 3px;
    background: var(--green);
  }
  .contact-list {
    position: absolute; right: 36px; top: 142px;
    list-style: none;
    color: #333;
    font-size: 15px;
    line-height: 24px;
  }
  .contact-list li { display: flex; align-items: center; gap: 8px; }
  .contact-list svg { width: 12px; height: 12px; flex: none; }
  .front-band {
    position: absolute; left: 0; bottom: 0;
    width: 100%; height: 34px;
    background: var(--navy);
  }

  /* Back */
  .card-back { left: 570px; top: 590px; background: linear-gradient(180deg, var(--paper) 0%, var(--paper-grey) 100%); }
  .back-panel {
    position: absolute; left: 0; top: 0;
    width: 100%; height: 200px;
    background: linear-gradient(180deg, #2a5c8c 0%, var(--navy) 40%, var(--navy-deep) 100%);
  }
  .back-spine {
    position: absolute; right: 40px; top: 0;
    width: 300px; height: 70px;
    background: radial-gradient(ellipse at 50% 20%, rgba(120,160,200,0.45) 0%, rgba(13,74,128,0) 70%);
  }
  .back-brand {
    position: absolute; left: 40px; top: 70px;
    color: var(--paper);
    font-weight: 400;
    font-size: 44px;
    line-height: 1.05;
    letter-spacing: 2px;
    text-transform: uppercase;
  }
  .back-brand span { display: block; font-size: 32px; letter-spacing: 6px; }
  .back-rule {
    position: absolute; left: 0; top: 200px;
    width: 100%; height: 7px;
    background: var(--green-soft);
  }
  .appointment {
    position: absolute; left: 40px; top: 222px;
    color: var(--ink);
    font-size: 14px;
    line-height: 21px;
    letter-spacing: 0.5px;
    text-transform: uppercase;
  }
</style>
</head>
<body>

<section class="card card-front" aria-label="Business card front">
  <div class="front-spine" role="img" aria-label="Photograph of spine vertebrae"></div>
  <div class="front-brand">Meridian<span>Chiropractic</span></div>
  <div class="person">
    <div class="person-name">YOUR NAME</div>
    <div class="person-role">Postions</div>
  </div>
  <div class="accent-tab"></div>
  <ul class="contact-list">
    <li>
      <svg viewBox="0 0 12 12"><path d="M6 0.5a4 4 0 0 1 4 4c0 3-4 7-4 7s-4-4-4-7a4 4 0 0 1 4-4z" fill="var(--orange)"/><circle cx="6" cy="4.5" r="1.5" fill="#fff"/></svg>
      Your Local Address
    </li>
    <li>
      <svg viewBox="0 0 12 12"><rect x="3" y="0.5" width="6" height="11" rx="1.2" fill="none" stroke="var(--orange)" stroke-width="1.4"/></svg>
      xxx-xxx-xxxx
    </li>
    <li>
      <svg viewBox="0 0 12 12"><rect x="0.5" y="2" width="11" height="8" rx="1" fill="var(--orange)"/><path d="M1 2.5l5 4 5-4" fill="none" stroke="#fff" stroke-width="1"/></svg>
      info@meridianchiro.com
    </li>
    <li>
      <svg viewBox="0 0 12 12"><circle cx="6" cy="6" r="5.2" fill="none" stroke="var(--orange)" stroke-width="1.3"/><path d="M0.8 6h10.4M6 0.8c-2.5 3-2.5 7.4 0 10.4M6 0.8c2.5 3 2.5 7.4 0 10.4" fill="none" stroke="var(--orange)" stroke-width="1"/></svg>
      Yourwebsite.com
    </li>
  </ul>
  <div class="front-band"></div>
</section>

<section class="card card-back" aria-label="Business card back">
  <div class="back-panel"></div>
  <div class="back-spine" role="img" aria-label="Faint photograph of spine vertebrae"></div>
  <div class="back-brand">Meridian<span>Chiropractic</span></div>
  <div class="back-rule"></div>
  <div class="appointment">
    <div>Your next appointment</div>
    <div>Date:</div>
    <div>Time:</div>
  </div>
</section>

</body>
</html>
```